Ostrander Granite Hall Museum Website (Design Only)

The Ostrander Granite Hall is a newly renovated historical building in lower Manhattan. We are building a website for them so that tours and events can be scheduled. We have provided typography requirements along with many photographs. You are free to be creative with the use of the photographs in your design. There is no specific brand or color guidelines but the client did specify that they wanted the website to be clean, simple and elegant BUT to also reflect the vintage colors and feeling of the building. Please do NOT design the logo as we have a separate contest for the logo. We have provided a mock up of all website pages that we would like designed. however we encourage you to design and submit the home page an a few other pages first so we can provide feedback. The designs that you provide must be compatible with Wix.

```html
<!DOCTYPE html>
<html lang="en">
<head>
<meta charset="utf-8">
<title>Ostrander Granite Hall</title>
<link href="https://fonts.googleapis.com/css2?family=Baloo+2:wght@600&family=IBM+Plex+Sans:wght@400&display=swap" rel="stylesheet">
<style>
:root{
  --cream:#f1ecce;
  --header:#ece6c2;
  --teal:#74bfa6;
  --coral:#cd6b4b;
  --ink:#1e1a14;
  --white:#ffffff;
}
*{box-sizing:border-box;margin:0;padding:0}
html,body{width:1091px;height:1200px;overflow:hidden}
body{position:relative;background:var(--cream);font-family:"IBM Plex Sans",sans-serif;color:var(--ink)}
.display{font-family:"Baloo 2",sans-serif;font-weight:600}

.site-header{position:absolute;top:0;left:0;width:1091px;height:64px;background:var(--header);z-index:3}
.nav-link{position:absolute;top:22px;font-size:14px;color:#3a342a}
.btn{display:flex;align-items:center;justify-content:center;background:var(--teal);color:var(--white);border-radius:30px;font-family:"Baloo 2",sans-serif;font-weight:600;letter-spacing:-.3px}
.header-btn{position:absolute;left:899px;top:16px;width:91px;height:33px;font-size:14px}

.brand-tab{position:absolute;left:444px;top:0;width:203px;height:92px;background:var(--header);border-radius:0 0 60px 60px;z-index:3;display:flex;align-items:center;justify-content:center;gap:8px}
.brand-mark{width:14px;height:14px;background:var(--ink)}
.brand-name{font-family:"Baloo 2",sans-serif;font-weight:600;font-size:19px;line-height:20px;color:var(--ink)}

.hero-photo{position:absolute;top:64px;left:0;width:1091px;height:600px;background:linear-gradient(180deg,#3a3a3a 0%,#5a5a5a 35%,#2c2c2c 70%,#1a1a1a 100%)}
.hero-edge{position:absolute;top:600px;left:0;width:1091px;height:140px}
.hero-copy{position:absolute;left:101px;top:245px;width:600px;color:var(--white);z-index:2}
.hero-title{font-size:44px;line-height:54px;letter-spacing:-1.2px;white-space:nowrap}
.hero-text{margin-top:12px;font-size:13.5px;line-height:24px;width:400px}
.hero-btn{margin-top:18px;width:100px;height:42px;font-size:14px}

.feature{position:absolute;top:793px;width:250px;height:250px;border-radius:50%;overflow:hidden}
.feature-hours{left:126px;background:linear-gradient(160deg,#d8d8d8,#6a6a6a 60%,#2a2a2a)}
.feature-see{left:421px;background:var(--coral);opacity:.95;display:flex;flex-direction:column;align-items:center;justify-content:center;text-align:center;color:var(--white)}
.feature-history{left:716px;background:linear-gradient(170deg,#9fb8cf 0%,#8a6a45 45%,#5a3f24 100%)}
.feature-cap{position:absolute;left:12%;width:76%;top:172px;height:160px;border-radius:50%;background:var(--teal);text-align:center;color:var(--white);font-size:34px;line-height:50px;padding-top:8px;letter-spacing:-.8px}
.see-title{font-size:34px;line-height:38px;letter-spacing:-.8px}
.see-text{font-size:13.5px;line-height:23px;margin-top:4px;width:160px}
.see-link{font-size:16px;margin-top:6px;letter-spacing:-.3px}

.site-footer{position:absolute;left:0;top:1130px;width:1091px;height:70px;background:var(--coral);color:var(--white);display:flex;align-items:center;justify-content:center;font-size:14px}
</style>
</head>
<body>
<header class="site-header">
  <a class="nav-link" style="left:102px">About the Building</a>
  <a class="nav-link" style="left:241px">Calendar</a>
  <a class="nav-link" style="left:322px">Public Exhibitions</a>
  <a class="nav-link" style="left:658px">Tour the Building</a>
  <a class="nav-link" style="left:788px">Plan Your Visit</a>
  <a class="btn header-btn">Contact Us</a>
</header>
<div class="brand-tab">
  <span class="brand-mark"></span>
  <span class="brand-name">Ostrander<br>Granite<br>Hall</span>
</div>

<div class="hero-photo" role="img" aria-label="Black and white photograph of the historic ferry terminal facade with tall windows and balcony"></div>
<svg class="hero-edge" viewBox="0 0 1091 140" preserveAspectRatio="none">
  <path fill="var(--cream)" d="M0 20 C60 40 90 70 110 110 C120 135 125 100 135 90 C170 60 220 90 270 70 C320 55 360 75 420 60 C480 45 520 70 580 55 C640 40 700 60 760 50 C820 40 860 70 900 80 C940 88 980 60 1020 40 C1050 25 1070 10 1091 5 L1091 140 L0 140 Z"/>
</svg>

<section class="hero-copy">
  <h1 class="hero-title display">Welcome to the Ostrander<br>Granite Hall</h1>
  <p class="hero-text">The majestic Ostrander Granite Hall is located at the southern tip of Manhattan. Built in 1909, the building is the last remaining historic working ferry terminal in New York City.</p>
  <a class="btn hero-btn">Contact Us</a>
</section>

<div class="feature feature-hours" role="img" aria-label="Black and white photograph of ornate ironwork detail">
  <div class="feature-cap display">Hours</div>
</div>
<div class="feature feature-see">
  <div class="see-title display">What to see</div>
  <p class="see-text">Our building hosts exhibitions of all kinds.</p>
  <div class="see-link display">Exhibitions &raquo;</div>
</div>
<div class="feature feature-history" role="img" aria-label="Photograph of the ornate terminal facade against a blue sky">
  <div class="feature-cap display">History</div>
</div>

<footer class="site-footer">©Copyrights 2022 Ostrander Granite Hall &nbsp;&nbsp;|&nbsp;&nbsp; All Rights Reserved</footer>
</body>
</html>
```